Business Card Design for The Lending Nook Inc.

We need a business card design for our mortgage company: "The Lending Nook Inc."

Need to have Social Media Account on there as a possibility

Industry/Entity Type

Business

```html
<!DOCTYPE html>
<html lang="en">
<head>
<meta charset="utf-8">
<title>The Lending Nook Inc. – Business Card</title>
<link href="https://fonts.googleapis.com/css2?family=Open+Sans:ital,wght@0,400;0,600;0,700;1,400&display=swap" rel="stylesheet">
<style>
  :root {
    --brand-blue: #0d5aad;
    --brand-blue-deep: #0a4a92;
    --ink-grey: #55585c;
    --mark-grey: #7d7f82;
    --paper: #ffffff;
    --backdrop: #e9e7e3;
  }
  * { box-sizing: border-box; margin: 0; padding: 0; }
  html, body { width: 1200px; height: 892px; overflow: hidden; }
  body {
    background: var(--backdrop);
    font-family: "Open Sans", Arial, sans-serif;
    display: flex;
    flex-direction: column;
    align-items: center;
    justify-content: center;
    gap: 60px;
  }
  .card {
    position: relative;
    width: 620px;
    height: 354px;
    overflow: hidden;
    box-shadow: 0 6px 18px rgba(0,0,0,0.18);
  }

  /* Front */
  .card--front { background: var(--brand-blue); color: var(--paper); }
  .brand {
    position: absolute;
    display: flex;
    align-items: center;
    gap: 14px;
  }
  .card--front .brand { left: 50%; top: 50%; transform: translate(-50%, -60%); }
  .brand__dot {
    width: 54px; height: 54px;
    border-radius: 50%;
    border: 4px solid currentColor;
    flex: none;
  }
  .brand__text { display: flex; flex-direction: column; line-height: 1; }
  .brand__name { font-size: 36px; font-weight: 600; letter-spacing: 0.2px; }
  .brand__suffix { font-size: 11px; font-weight: 600; letter-spacing: 5px; margin-top: 6px; align-self: flex-end; }
  .front__accent {
    position: absolute;
    right: -34px; bottom: -40px;
    width: 170px; height: 170px;
    border-radius: 50%;
    border: 6px solid var(--brand-blue-deep);
    opacity: 0.8;
  }

  /* Back */
  .card--back { background: var(--paper); }
  .back__accent {
    position: absolute;
    left: 30px; top: -70px;
    width: 190px; height: 190px;
    border-radius: 50%;
    border: 7px solid var(--mark-grey);
  }
  .card--back .brand { left: 250px; top: 92px; color: var(--brand-blue); gap: 10px; }
  .card--back .brand__dot { width: 40px; height: 40px; border-width: 3px; border-color: var(--ink-grey); }
  .card--back .brand__name { font-size: 26px; }
  .card--back .brand__suffix { font-size: 8px; letter-spacing: 4px; color: var(--ink-grey); }
  .person { position: absolute; left: 200px; top: 168px; }
  .person__name { color: var(--brand-blue); font-size: 22px; font-weight: 700; letter-spacing: 1.5px; text-transform: uppercase; }
  .person__title { color: #333; font-size: 13px; font-style: italic; margin-top: 4px; margin-left: 20px; }
  .contact-band {
    position: absolute;
    left: 0; right: 0; bottom: 0;
    height: 78px;
    background: var(--brand-blue);
    display: flex;
    align-items: center;
    justify-content: space-around;
    padding: 0 20px;
    list-style: none;
  }
  .contact-band__item { display: flex; align-items: center; gap: 10px; color: var(--paper); font-size: 13px; }
  .contact-band__item svg { width: 18px; height: 18px; fill: none; stroke: var(--paper); stroke-width: 1.6; }
</style>
</head>
<body>
  <section class="card card--front" aria-label="Card front">
    <div class="brand">
      <span class="brand__dot"></span>
      <span class="brand__text">
        <span class="brand__name">The Lending Nook</span>
        <span class="brand__suffix">INC</span>
      </span>
    </div>
    <span class="front__accent"></span>
  </section>

  <section class="card card--back" aria-label="Card back">
    <span class="back__accent"></span>
    <div class="brand">
      <span class="brand__dot"></span>
      <span class="brand__text">
        <span class="brand__name">The Lending Nook</span>
        <span class="brand__suffix">INC</span>
      </span>
    </div>
    <div class="person">
      <p class="person__name">Your Name</p>
      <p class="person__title">Title</p>
    </div>
    <ul class="contact-band">
      <li class="contact-band__item">
        <svg viewBox="0 0 24 24"><rect x="3" y="9" width="18" height="12" rx="2"/><path d="M6 9V4h12v5"/><circle cx="12" cy="15" r="2.5"/></svg>
        +1 555 014 7290
      </li>
      <li class="contact-band__item">
        <svg viewBox="0 0 24 24"><rect x="7" y="2" width="10" height="20" rx="2"/><path d="M11 18h2"/></svg>
        +1 555 014 7290
      </li>
      <li class="contact-band__item">
        <svg viewBox="0 0 24 24"><circle cx="12" cy="12" r="4"/><path d="M16 12v1.5a2.5 2.5 0 0 0 5 0V12a9 9 0 1 0-4 7.5"/></svg>
        person@lendingnook.com
      </li>
    </ul>
  </section>
</body>
</html>
```